■依頼の目的/概要
当方販促で使用するメモ帳を販売しております。
今回は年末年始に企業様が挨拶に出向く時に使用するノベルティメモ帳の表紙及び本文のデザインをお願いします。

■依頼詳細
2021年の干支である「丑」がデザインされた表紙とメモ部分のデザイン依頼です。使われる企業様は全国の企業様さまざまです。過去2年の実績デザインを添付しております。
毎年多数の良いデザインがありますので複数点採用しております。
デザインによりましては添付のテンプレート以外での修正があります。ご了承下さい。

■重視するポイント
色使いなど制限はありませんが、年末年始向けの貰ってうれしい配って嬉しいデザインを要望します。テンプレートを添付しておりますのでご利用下さい。

その他何かご不明な点がございましたら、お気軽にご質問下さい。
よろしくお願いいたします。

社内アンケートを行って決定しました。シンプルでインパクトのあるデザインが選ばれたようです。

今年もたくさんのポルテンの皆様のご提案ありがとうございます。せっかく時間を割いて提案して下さったにも関わらず選択されなかったポルテン様には申し訳けなく思っております。また機会があればご提案下さいませ。今回のご提案ありがとうございました。

```html
<!DOCTYPE html>
<html lang="en">
<head>
<meta charset="utf-8">
<title>2021 Memo Pad Cover</title>
<link rel="stylesheet" href="https://fonts.googleapis.com/css2?family=Noto+Serif:wght@700&family=Noto+Sans:wght@500&family=Nunito:wght@800&display=swap">
<style>
  :root {
    --paper: #ffffff;
    --pattern-red: #ec1c1c;
    --pattern-mid: #f46a6a;
    --badge-yellow: #f6c12e;
    --badge-red: #e8201a;
    --badge-orange: #f18a1d;
    --year-gold: #f9d54a;
    --cow-brown: #8b5a2b;
    --cow-white: #f3efe8;
    --label-white: #ffffff;
  }
  html, body {
    margin: 0;
    padding: 0;
    width: 1200px;
    height: 2444px;
    overflow: hidden;
    background: var(--paper);
  }
  .cover {
    position: relative;
    width: 1200px;
    height: 2444px;
    overflow: hidden;
  }
  .cow-pattern {
    position: absolute;
    inset: 0;
    background:
      linear-gradient(165deg,
        var(--pattern-red) 0%,
        var(--pattern-mid) 22%,
        var(--paper) 42%,
        var(--pattern-mid) 58%,
        var(--pattern-red) 78%,
        var(--pattern-mid) 100%);
  }
  .badge {
    position: absolute;
    left: 0;
    top: 0;
    width: 1200px;
    height: 2444px;
  }
  .year {
    font-family: "Noto Serif", Georgia, serif;
    font-weight: 700;
    font-size: 124px;
    fill: var(--year-gold);
    letter-spacing: 4px;
  }
  .memo-label {
    font-family: "Noto Sans", Arial, sans-serif;
    font-weight: 500;
    font-size: 50px;
    fill: var(--badge-red);
  }
  .greeting {
    font-family: "Nunito", Arial, sans-serif;
    font-weight: 800;
    font-size: 46px;
    fill: var(--label-white);
    letter-spacing: 12px;
  }
</style>
</head>
<body>
<main class="cover">
  <div class="cow-pattern" role="img" aria-label="Bold red cow-spot pattern on white covering the whole cover"></div>

  <svg class="badge" viewBox="0 0 1200 2444" xmlns="http://www.w3.org/2000/svg">
    <defs>
      <path id="greeting-arc" d="M 236 1960 A 372 372 0 0 0 964 1960"/>
      <linearGradient id="cow-tone" x1="0" y1="0" x2="1" y2="1">
        <stop offset="0" stop-color="var(--cow-white)"/>
        <stop offset="0.5" stop-color="#d9c2a4"/>
        <stop offset="1" stop-color="var(--cow-white)"/>
      </linearGradient>
    </defs>

    <circle class="badge-ring" cx="600" cy="1880" r="480" fill="var(--badge-yellow)"/>
    <circle class="badge-face" cx="600" cy="1880" r="428" fill="var(--badge-red)"/>
    <circle class="badge-sun" cx="600" cy="1830" r="230" fill="var(--badge-orange)"/>

    <text class="year" x="600" y="1612" text-anchor="middle">2021</text>

    <rect class="cow-art cow-art-left" x="192" y="1700" width="310" height="212" rx="10"
          fill="url(#cow-tone)"
          role="img" aria-label="Two brown and white cows holding the memo sign"/>
    <rect class="cow-art cow-art-right" x="698" y="1700" width="310" height="212" rx="10"
          fill="url(#cow-tone)"
          role="img" aria-label="Two brown and white cows holding the memo sign"/>

    <rect class="memo-sign" x="474" y="1772" width="252" height="168" fill="var(--label-white)"
          stroke="var(--cow-brown)" stroke-width="4"/>
    <text class="memo-label" x="600" y="1844" text-anchor="middle">memo</text>
    <text class="memo-label" x="600" y="1906" text-anchor="middle">pad</text>

    <text class="greeting">
      <textPath href="#greeting-arc" startOffset="50%" text-anchor="middle">hope your happy year</textPath>
    </text>
  </svg>
</main>
</body>
</html>
```